Graphic Design - Website Header - Leaderboard

Hello,
I am looking for a design to go above the navigation on my website/blog. Design will include an image, name of website and some followup wording or taglines.

Website will be a pagecraft blog about mens lifestyle, but will be more rugged in nature, the anti-VR blog for men. A man's man blog - think Kestwick Rider image. Inspiring young men about women, whiskey, boots, jeans & proper manners .. that sort of thing. Want to appeal to cosmopolitan men .. not actual cowboys, so no cowboy hats.

Would like an image on the left of the face of a tough looking, handsome man, looking into the page, with scruff. Man must be a drawing or abstract image, no photo.

Image should be at least 900 x 200 pixels and use earth tones. Navigation under image will be something like - About, Lifestyle, Attire, Transport, Man Skills, Booze, Women, Contact.

Name of blog will be TheHardyFellow.example
Updates

Serious about a legit design .. cmon people . this is an easy one ...please read my detailed brief.  Let me know if you have questions.... and, THANK YOU !

Reason: still looking for designs .. very detailed specs in the brief Thank You !

Target Market(s)

23-40yr old men, looking for tips on how to look and act like a cool guy and appeal to women

Industry/Entity Type

Graphic Design

Requirements
Must have
• 1. Drawing of a Man with scruff on left side of graphic, looking into the page (to the right). Not a photograph - an image or drawing. See uploaded image - want something ssimilar in style.

2. Masculine Earth Tones & Fonts. textured background

3. Include name of site in middle ..with tagline below it
"Inspiring Men About Women, Whiskey & Proper Manners"
(ability to easily change the tagline)
Nice to have
• Ability to easily use this design on a business card
Should not have
• 1. Actual photo of man
2. Shirtless guy
3. Cowboy hat or cigarette

```html
<!DOCTYPE html>
<html lang="en">
<head>
<meta charset="utf-8">
<title>TheHardyFellow.example — Header</title>
<link rel="stylesheet" href="https://fonts.googleapis.com/css2?family=Arvo:wght@700&family=Oswald:wght@600&family=Courier+Prime&display=swap">
<style>
  :root {
    --page-bg: #070302;
    --guide: #2a2520;
    --guide-text: #3a342e;
    --sky: #7a9cc4;
    --sand-light: #b89a76;
    --sand-mid: #8c6a48;
    --sand-dark: #4a3424;
    --skin: #c99a78;
    --plate: #2b2826;
    --plate-edge: #6a5e54;
    --title: #8a7a6c;
    --tagline: #ffffff;
    --tab-top: #5c4d40;
    --tab-bottom: #3a2f27;
    --tab-edge: #d7781e;
    --footer-band: #2e2824;
  }
  html, body {
    margin: 0;
    width: 1200px;
    height: 1000px;
    overflow: hidden;
    background: var(--page-bg);
  }
  .canvas { position: relative; width: 1200px; height: 1000px; }

  .guide-label {
    position: absolute;
    font-family: "Courier Prime", monospace;
    font-size: 12px;
    color: var(--guide-text);
    background: var(--page-bg);
    line-height: 1;
  }
  .guides { position: absolute; left: 0; top: 0; }

  .header {
    position: absolute;
    left: 150px; top: 384px;
    width: 900px; height: 233px;
    overflow: hidden;
  }
  .scene {
    position: absolute; inset: 0 0 21px 0;
    background:
      linear-gradient(180deg, var(--sky) 0%, #9aa9b8 22%, var(--sand-light) 34%, var(--sand-mid) 65%, var(--sand-dark) 100%);
  }
  .portrait {
    position: absolute; left: 0; top: 0;
    width: 190px; height: 212px;
    background: radial-gradient(ellipse at 45% 55%, var(--skin) 0%, #a47a5c 45%, rgba(140,106,72,0) 80%);
  }
  .title-plate {
    position: absolute; left: 216px; top: 7px;
    width: 680px; height: 133px;
  }
  .site-name {
    position: absolute; left: 216px; top: 7px;
    width: 680px; height: 133px;
    box-sizing: border-box;
    padding: 0 24px;
    display: flex; align-items: center; justify-content: center;
    margin: 0;
    font-family: "Arvo", serif;
    font-weight: 700;
    font-size: 44px;
    white-space: nowrap;
    color: var(--title);
  }
  .tagline {
    position: absolute; left: 216px; top: 146px;
    width: 684px;
    margin: 0;
    text-align: center;
    font-family: "Arvo", serif;
    font-weight: 700;
    font-size: 21px;
    white-space: nowrap;
    color: var(--tagline);
    text-shadow: 0 0 3px #000, 1px 1px 0 #000;
  }
  .footer-band {
    position: absolute; left: 0; bottom: 0;
    width: 142px; height: 21px;
    background: var(--footer-band);
  }
  .main-nav {
    position: absolute; left: 142px; top: 200px;
    width: 758px;
    height: 33px;
    display: flex; gap: 2px;
  }
  .main-nav a {
    box-sizing: border-box;
    flex: none;
    display: flex; align-items: center; justify-content: center;
    height: 33px;
    border: 1px solid var(--tab-edge);
    border-bottom: none;
    background: linear-gradient(180deg, var(--tab-top), var(--tab-bottom));
    clip-path: polygon(8px 0, 100% 0, 100% 100%, 0 100%, 0 8px);
    font-family: "Oswald", sans-serif;
    font-weight: 600;
    font-size: 14px;
    letter-spacing: 0.5px;
    color: #fff;
    text-decoration: none;
    text-transform: uppercase;
    white-space: nowrap;
  }
</style>
</head>
<body>
<div class="canvas">
  <svg class="guides" width="1200" height="1000" aria-hidden="true">
    <line x1="150" y1="363.5" x2="1050" y2="363.5" stroke="var(--guide)"/>
    <line x1="1069.5" y1="384" x2="1069.5" y2="586" stroke="var(--guide)"/>
    <line x1="1078.5" y1="588" x2="1078.5" y2="617" stroke="var(--guide)"/>
    <line x1="1078" y1="601.5" x2="1110" y2="601.5" stroke="var(--guide)"/>
  </svg>
  <span class="guide-label" style="left:577px;top:356px;padding:0 3px;">900 px</span>
  <span class="guide-label" style="left:1050px;top:479px;transform:rotate(90deg);padding:0 3px;">200 px</span>
  <span class="guide-label" style="left:1102px;top:595px;text-align:center;width:68px;background:none;">13 px<br>navigation</span>

  <header class="header">
    <div class="scene" role="img" aria-label="Rocky desert landscape under a pale blue sky"></div>
    <div class="portrait" role="img" aria-label="Portrait of a rugged dark-haired man with stubble looking to the right"></div>

    <svg class="title-plate" viewBox="0 0 680 133" aria-hidden="true">
      <polygon points="14,1 666,1 679,14 679,119 666,132 14,132 1,119 1,14"
               fill="var(--plate)" stroke="var(--plate-edge)" stroke-width="2"/>
    </svg>
    <h1 class="site-name">TheHardyFellow.example</h1>
    <p class="tagline">"Inspiring Men About Women, Whiskey &amp; Proper Manners”</p>

    <div class="footer-band"></div>
    <nav class="main-nav">
      <a href="#" style="width:80px">About</a>
      <a href="#" style="width:106px">Lifestyle</a>
      <a href="#" style="width:82px">Attire</a>
      <a href="#" style="width:118px">Transport</a>
      <a href="#" style="width:117px">Man Skills</a>
      <a href="#" style="width:75px">Booze</a>
      <a href="#" style="width:81px">Women</a>
      <a href="#" style="width:85px">Skills</a>
    </nav>
  </header>
</div>
</body>
</html>
```